Presentation and Communication Coaching Services Business needs updated interactive web site

I want to keep the color scheme, functionality, and pages of my current site, but with a newer/updated look. I need to improve security and simplify images, etc. (Please see current site http://brackwellvoicetutor.com ) This will need be functional on mobile devices, as well.

I'm attached to the scrolling client list and scrolling client feedback.

Industry/Entity Type

Professional Service

Font styles to use
Sans Serif

Colors
0356a4
f37122
33a6d7

Requirements
Must have
• scrolling client banner on home page, client comments slider, color scheme
• Please see current site: http://brackwellvoicetutor.com
Nice to have
• better action/appearance
Should not have
• I don't want it to look like all the other sites/templates

```html
<!DOCTYPE html>
<html lang="en">
<head>
<meta charset="utf-8">
<title>Brackwell Voice Tutor</title>
<link href="https://fonts.googleapis.com/css2?family=Open+Sans:ital,wght@0,400;0,600;0,700;1,400&family=Courgette&display=swap" rel="stylesheet">
<style>
  :root {
    --ink: #2f3033;
    --text: #3b3c3f;
    --white: #ffffff;
    --gold: #d6a122;
    --gold-glass: rgba(190, 143, 22, 0.86);
    --teal: #5fcfd9;
    --teal-deep: #2fc0cf;
    --rule: #c9c9c9;
  }
  * { margin: 0; padding: 0; box-sizing: border-box; }
  html, body { width: 1182px; height: 1200px; overflow: hidden; background: var(--white); }
  body { position: relative; font-family: "Open Sans", Arial, sans-serif; color: var(--text); }

  .hero {
    position: absolute; left: 12px; top: 0; width: 1159px; height: 572px;
    background:
      radial-gradient(ellipse at 78% 45%, rgba(120,110,120,0.55) 0%, rgba(0,0,0,0) 40%),
      radial-gradient(ellipse at 92% 40%, rgba(190,40,80,0.55) 0%, rgba(0,0,0,0) 30%),
      radial-gradient(ellipse at 25% 85%, rgba(150,70,70,0.55) 0%, rgba(0,0,0,0) 45%),
      linear-gradient(180deg, #0b0b12 0%, #1b1620 55%, #2a1a1c 100%);
  }
  .brand {
    position: absolute; left: 29px; top: 22px;
    font-size: 24px; font-weight: 400; color: var(--white); letter-spacing: -0.3px;
    white-space: nowrap;
  }
  .phone {
    position: absolute; right: 37px; top: 20px;
    display: flex; align-items: center; gap: 6px;
    font-size: 19px; color: var(--white); white-space: nowrap;
  }
  .nav {
    position: absolute; right: 37px; top: 57px;
    display: flex; gap: 22px; list-style: none;
    font-size: 14.5px; color: var(--white); letter-spacing: 0.1px;
    white-space: nowrap;
  }
  .nav .active { font-weight: 600; }
  .social {
    position: absolute; left: 37px; top: 112px;
    display: flex; flex-direction: column; gap: 17px; list-style: none;
  }
  .social li { width: 13px; height: 13px; display: block; }
  .social .dot { border-radius: 50%; background: var(--white); }
  .hero-quote {
    position: absolute; left: 146px; top: 161px; width: 436px; height: 184px;
    background: var(--gold-glass); border-radius: 8px;
    padding: 18px 16px 0 12px;
    font-style: italic; font-size: 12.5px; line-height: 21px; color: var(--white);
  }
  .hero-quote .open {
    float: left; font-family: Georgia, serif; font-style: normal; font-weight: 700;
    font-size: 56px; line-height: 44px; height: 30px; margin: 0 8px 0 2px; color: var(--white);
  }
  .hero-quote .close {
    font-family: Georgia, serif; font-style: normal; font-weight: 700;
    font-size: 44px; line-height: 0; vertical-align: -16px; margin-left: 6px; color: var(--white);
  }

  .intro-title {
    position: absolute; left: 158px; top: 652px;
    font-family: "Courgette", cursive; font-weight: 400;
    font-size: 35px; line-height: 40px; color: var(--ink); white-space: nowrap;
  }
  .intro-copy {
    position: absolute; left: 158px; top: 752px; width: 456px;
    font-size: 13.4px; line-height: 21.6px; text-align: justify; color: var(--text);
  }
  .intro-photo {
    position: absolute; left: 642px; top: 616px; width: 381px; height: 453px;
    background: linear-gradient(120deg, #e8e6e2 0%, #cfcac4 30%, #b8322c 55%, #a32a26 100%);
  }
  .pull-quote {
    position: absolute; left: 158px; top: 910px; width: 530px; height: 122px;
    background: var(--gold); padding: 32px 20px 0 20px;
    font-family: "Courgette", cursive; font-size: 16.4px; line-height: 23px; color: var(--white);
  }

  .divider { position: absolute; left: 0; top: 1104px; width: 1182px; height: 2px; background: var(--rule); }
  .services-title {
    position: absolute; left: 0; top: 1118px; width: 1182px; text-align: center;
    font-size: 36px; font-weight: 700; color: var(--ink);
  }
  .service-badge { position: absolute; left: 158px; top: 1139px; }
  .service-badge .num {
    position: absolute; left: 50px; top: 16px; width: 60px; text-align: center;
    font-size: 26px; font-weight: 600; color: var(--white);
    border-bottom: 2px solid var(--white); line-height: 34px;
  }
  .service-badge .label {
    position: absolute; left: 38px; top: 56px; width: 84px; text-align: center;
    font-size: 11px; color: var(--white); letter-spacing: 1px;
  }
  .service-name {
    position: absolute; left: 810px; top: 1170px;
    font-size: 46px; font-weight: 700; color: var(--teal-deep); letter-spacing: 3px;
  }
</style>
</head>
<body>
  <header class="hero" role="img" aria-label="Speaker in a dark suit addressing a large seated audience on a stage with coloured lights">
    <div class="brand">brackwellvoicetutor</div>
    <div class="phone">
      <svg width="16" height="16" viewBox="0 0 24 24" aria-hidden="true"><path fill="#fff" d="M6.6 10.8a15.1 15.1 0 0 0 6.6 6.6l2.2-2.2a1 1 0 0 1 1-.25 11.4 11.4 0 0 0 3.6.57 1 1 0 0 1 1 1V20a1 1 0 0 1-1 1A17 17 0 0 1 3 4a1 1 0 0 1 1-1h3.5a1 1 0 0 1 1 1c0 1.25.2 2.45.57 3.57a1 1 0 0 1-.25 1z"/></svg>
      <span>555.014.2236</span>
    </div>
    <ul class="nav">
      <li class="active">HOME</li>
      <li>ABOUT US</li>
      <li>CLIENTS</li>
      <li>REVIEWS</li>
      <li>SERVICES</li>
      <li>CONTACT</li>
      <li>SPEAKING SECRETS</li>
    </ul>
    <ul class="social">
      <li class="dot"></li>
      <li class="dot"></li>
      <li class="dot"></li>
      <li>
        <svg width="14" height="14" viewBox="0 0 14 14" aria-hidden="true"><circle cx="11" cy="2.5" r="2.3" fill="#fff"/><circle cx="2.5" cy="7" r="2.3" fill="#fff"/><circle cx="11" cy="11.5" r="2.3" fill="#fff"/><path d="M11 2.5 2.5 7 11 11.5" stroke="#fff" stroke-width="1.4" fill="none"/></svg>
      </li>
    </ul>
    <blockquote class="hero-quote"><span class="open">&ldquo;</span>&ldquo;I think my talk went very well . . . and I felt that I had their full attention. I felt comfortable and prepared at the start. I just jumped in and spoke without my notes. I didn&rsquo;t fumble at all . . . I felt I was able to talk through my outline smoothly and naturally with good, logical transitions . . . After my talk . . . my boss, the president of my company came up to me and said, &ldquo;Excellent! On all points!<span class="close">&rdquo;</span></blockquote>
  </header>

  <section class="intro">
    <h1 class="intro-title">You&rsquo;re good at what you do.<br>Learn How to let it show.</h1>
    <p class="intro-copy">An individual works hard to reach a place of respect and authority in her or his chosen profession. Effective self-presentation adds confidence and allows one&rsquo;s unique personality and expertise to shine through &ndash; in fact, it is key in separating from the pack and reaching higher goals. As competition increases, these skills become more essential in demonstrating value to an employer, manager, or board.</p>
    <div class="intro-photo" role="img" aria-label="Coaching session: a presenter at a flip chart speaking to a seated colleague in a red meeting room"></div>
    <div class="pull-quote">&ldquo;You&rsquo;ve done your best to reach this professional level. It&rsquo;s time to develop what it takes to reach the next one.&rdquo;</div>
  </section>

  <div class="divider"></div>

  <section class="services">
    <h2 class="services-title">Our Services</h2>
    <div class="service-badge">
      <svg width="160" height="61" viewBox="0 0 160 61" aria-hidden="true"><path d="M0 0 A190 190 0 0 1 160 61 L0 61 Z" fill="var(--teal)"/></svg>
      <span class="num">01</span>
      <span class="label">COACHING</span>
    </div>
    <div class="service-name">COACHING</div>
  </section>
</body>
</html>
```